Aerospace Private Equity Firm Needs Website

We need a website for new private equity fund called Corvin Partners. We buy smaller companies in the aerospace and industrial industries. I have attached some information about the firm. An example of a site we like that is a similar business but focused in a different sector is www.tarnowcare.com. www.quillstonefunds.com is a firm that also invests in aerospace companies.

Industry/Entity Type

Equity

Number of Pages Required

1 page

Colors
0555a3
33a6d7
ec1f27

```html
<!DOCTYPE html>
<html lang="en">
<head>
<meta charset="utf-8">
<title>Corvin Partners</title>
<link href="https://fonts.googleapis.com/css2?family=Exo+2:wght@400;500;600&family=Tinos&display=swap" rel="stylesheet">
<style>
  :root {
    --brand-blue: #0555a3;
    --brand-navy: #073a80;
    --brand-red: #d0141c;
    --heading-blue: #3d6598;
    --ink: #111;
    --body-text: #333;
    --white: #fff;
    --rule: #d6d6d6;
  }
  * { margin: 0; padding: 0; box-sizing: border-box; }
  html, body { width: 1200px; height: 822px; overflow: hidden; background: var(--white); }
  .page { position: relative; width: 1200px; height: 822px; font-family: "Exo 2", sans-serif; color: var(--ink); }

  .site-header { position: absolute; left: 0; top: 0; width: 1200px; height: 134px; border-bottom: 1px solid var(--rule); }
  .brand { position: absolute; left: 92px; top: 22px; display: flex; align-items: center; gap: 10px; }
  .brand-mark { width: 16px; height: 16px; background: var(--brand-blue); }
  .brand-name { font-size: 34px; font-weight: 600; color: var(--brand-blue); letter-spacing: -0.5px; }

  .contacts { position: absolute; right: 94px; top: 24px; display: flex; gap: 18px; }
  .contact { display: flex; align-items: center; gap: 10px; }
  .contact-label { font-size: 13px; text-transform: uppercase; line-height: 1.1; }
  .contact-phone { font-size: 19px; line-height: 1.1; }

  .main-nav { position: absolute; left: 92px; top: 97px; width: 1013px; display: flex; justify-content: space-between; }
  .main-nav a { font-size: 17px; color: var(--ink); text-decoration: none; padding-bottom: 6px; position: relative; }
  .main-nav a.is-active { color: var(--brand-red); border-bottom: 1px solid var(--brand-red); }
  .main-nav a.is-active::after { content: ""; position: absolute; left: 50%; bottom: -1px; margin-left: -4px; border: 4px solid transparent; border-bottom-color: var(--brand-red); }

  .hero { position: absolute; left: 0; top: 135px; width: 1200px; height: 419px;
    background: linear-gradient(180deg, #4e6f95 0%, #8a97a4 35%, #d9c48e 62%, #b59a72 80%, #8e8a88 100%); }
  .hero-plane { position: absolute; left: 20px; top: 75px; width: 1150px; height: 330px;
    background: radial-gradient(ellipse at 62% 45%, rgba(220,224,230,.55), rgba(40,70,150,.25) 45%, transparent 70%); }
  .hero-arrow { position: absolute; top: 176px; width: 44px; height: 36px; background: rgba(255,255,255,.55); display: flex; align-items: center; justify-content: center; }
  .hero-arrow span { width: 34px; height: 28px; background: #333; display: flex; align-items: center; justify-content: center; }
  .hero-arrow.prev { left: 0; }
  .hero-arrow.next { right: 0; }
  .sector-bar { position: absolute; left: 0; bottom: 0; width: 1200px; height: 94px;
    background: linear-gradient(90deg, rgba(40,30,25,.15), rgba(40,30,25,.55) 30%, rgba(40,30,25,.55) 70%, rgba(40,30,25,.15)); }
  .sector { position: absolute; top: 15px; display: flex; align-items: center; gap: 8px; color: var(--white); font-size: 19px; font-weight: 500; }
  .sector-icon { width: 64px; height: 64px; border-radius: 50%; background: #2b2623; border: 2px solid #bbb; display: flex; align-items: center; justify-content: center; }
  .sector.aero { left: 367px; }
  .sector.industrial { left: 617px; }
  .sector.industrial .sector-label { margin-left: 7px; margin-top: 4px; }

  .intro { position: absolute; left: 92px; top: 566px; width: 1016px; text-align: center; }
  .intro h1 { font-size: 21px; font-weight: 500; color: var(--heading-blue); line-height: 30px; }
  .intro p { margin-top: 20px; font-family: "Tinos", serif; font-size: 16.3px; line-height: 24.5px; color: var(--body-text); }

  .site-footer { position: absolute; left: 0; top: 782px; width: 1200px; height: 40px; background: var(--brand-navy);
    color: var(--white); font-family: "Tinos", serif; font-size: 14px; text-align: center; line-height: 40px; }
</style>
</head>
<body>
<div class="page">
  <header class="site-header">
    <div class="brand"><span class="brand-mark"></span><span class="brand-name">Corvin Partners</span></div>
    <div class="contacts">
      <div class="contact">
        <svg width="40" height="34" viewBox="0 0 40 34"><circle cx="14" cy="19" r="13" fill="none" stroke="var(--brand-blue)" stroke-width="1.6"/><path d="M10 12c-2 3-1 8 3 12 2 2 4 2 5 1l-2-3-2 1c-2-2-3-4-2-6l2-1-2-4z" fill="var(--brand-blue)"/><circle cx="31" cy="7" r="6" fill="#fff" stroke="var(--brand-red)" stroke-width="1.2"/><text x="31" y="11" font-size="10" text-anchor="middle" fill="var(--brand-red)" font-family="Exo 2, sans-serif">1</text></svg>
        <div><div class="contact-label">Corvin Partners</div><div class="contact-phone">(310) 555-0147</div></div>
      </div>
      <div class="contact">
        <svg width="40" height="34" viewBox="0 0 40 34"><circle cx="14" cy="19" r="13" fill="none" stroke="#111" stroke-width="1.6"/><path d="M10 12c-2 3-1 8 3 12 2 2 4 2 5 1l-2-3-2 1c-2-2-3-4-2-6l2-1-2-4z" fill="#111"/><circle cx="31" cy="7" r="6" fill="#fff" stroke="var(--brand-red)" stroke-width="1.2"/><text x="31" y="11" font-size="10" text-anchor="middle" fill="var(--brand-red)" font-family="Exo 2, sans-serif">2</text></svg>
        <div><div class="contact-label">Halvern Capital</div><div class="contact-phone">(203) 555-0182</div></div>
      </div>
    </div>
    <nav class="main-nav">
      <a href="#" class="is-active">Home</a>
      <a href="#">Overview</a>
      <a href="#">Team</a>
      <a href="#">Investment Strategy</a>
      <a href="#">Investment Performance</a>
      <a href="#">Case Study</a>
      <a href="#">Contact Us</a>
    </nav>
  </header>

  <section class="hero">
    <div class="hero-plane" role="img" aria-label="Photograph of a regional passenger jet climbing through a golden sunset sky"></div>
    <div class="hero-arrow prev"><span><svg width="12" height="14" viewBox="0 0 12 14"><path d="M8 2L3 7l5 5" fill="none" stroke="#fff" stroke-width="2.5"/></svg></span></div>
    <div class="hero-arrow next"><span><svg width="12" height="14" viewBox="0 0 12 14"><path d="M4 2l5 5-5 5" fill="none" stroke="#fff" stroke-width="2.5"/></svg></span></div>
    <div class="sector-bar">
      <div class="sector aero">
        <span class="sector-icon"><svg width="30" height="30" viewBox="0 0 30 30"><path d="M24 5c1-1 2 0 1 1l-5 5 2 11-2 2-4-8-4 4 1 4-2 1-2-4-4-2 1-2 4 1 4-4-8-4 2-2 11 2z" fill="#fff"/></svg></span>
        <span class="sector-label">Aerospace Sector</span>
      </div>
      <div class="sector industrial">
        <span class="sector-icon"><svg width="30" height="30" viewBox="0 0 30 30"><path d="M4 24V12l6 4v-4l6 4v-4l6 4V6h4v18z" fill="none" stroke="#fff" stroke-width="2"/><path d="M8 20h2M13 20h2M18 20h2" stroke="#fff" stroke-width="2"/></svg></span>
        <span class="sector-label">Industrial Sector</span>
      </div>
    </div>
  </section>

  <section class="intro">
    <h1>Corvin Focuses on Lower Middle-market Control Investments In Aerospace And<br>Industrial Companies Based In North America.</h1>
    <p>Lorem ipsum dolor sit amet, consectetuer adipiscing elit, sed diam nonummy nibh euismod tincidunt ut laoreet dolore magna aliquam erat volutpat. Ut wisi enim ad minim veniam, quis nostrud exerci tation ullamcorper suscipit lobortis nisl ut aliquip ex ea commodo consequat. Duis autem vel eum iriure dolor in hendrerit in vulputate velit esse molestie consequat, vel illum dolore eu feugiat nulla facilisis at vero eros et accumsan et iusto odio dignissim qui blandit praesent luptatum zzril delenit augue duis dolore te feugait nulla facilisi.</p>
  </section>

  <footer class="site-footer">Copyright © 2017 Corvin Partners | Privacy Policy | User Agreement</footer>
</div>
</body>
</html>
```